BrightNest

Need a 6 page template designed in Layered PSD for a house cleaning company.

Target Market(s)

People who are selling their homes and need house cleaning

Industry/Entity Type

House cleaning

Number of Pages Required

5+ page

Font styles to use
Sans Serif

Requirements
Must have
• Please see the zip file included with the brief. It has a document with detailed instructions.

```html
<!DOCTYPE html>
<html lang="en">
<head>
<meta charset="utf-8">
<title>BrightNest – Available Cleaning Services</title>
<link href="https://fonts.googleapis.com/css2?family=Oswald:wght@500;600&family=Hind:wght@400;500;600&display=swap" rel="stylesheet">
<style>
:root{
  --navy:#1d4189;
  --navy-deep:#183877;
  --green:#76bd43;
  --text:#252a33;
  --soft:#f4f6fa;
  --white:#ffffff;
}
*{box-sizing:border-box;margin:0;padding:0}
html,body{width:1200px;height:3468px;overflow:hidden}
body{font-family:"Hind",sans-serif;color:var(--text);background:var(--white);position:relative}
.site-header{position:absolute;left:0;top:0;width:1200px;height:131px;background:var(--white)}
.brand{position:absolute;left:63px;top:46px;display:flex;align-items:center;gap:8px;font-family:"Hind",sans-serif;font-weight:600;font-size:28px;color:var(--navy)}
.brand-dot{width:14px;height:14px;border-radius:50%;background:var(--green)}
.main-nav a{position:absolute;top:53px;font-size:14px;color:var(--navy);text-decoration:none;font-weight:500}
.main-nav a.active{color:var(--green)}
.nav-mark{position:absolute;left:376px;top:36px;color:var(--green);font-size:12px}
.btn-phone,.btn-header{position:absolute;top:44px;height:37px;display:flex;align-items:center;justify-content:center;font-size:14px;color:var(--white);border-radius:2px}
.btn-phone{left:796px;width:162px;background:var(--green);gap:8px}
.btn-header{left:975px;width:163px;background:var(--navy)}
.hero{position:absolute;left:0;top:131px;width:1200px;height:335px;background:linear-gradient(100deg,#3457a2 0%,#2a4c97 45%,#3a5aa6 100%)}
.hero h1{position:absolute;left:0;right:0;top:134px;text-align:center;font-family:"Oswald",sans-serif;font-weight:500;font-size:48px;color:var(--white);letter-spacing:.3px}
.service{position:absolute;left:0;width:1200px}
.service.alt{background:var(--soft)}
.service h2{position:absolute;font-family:"Oswald",sans-serif;font-weight:600;font-size:40px;color:var(--navy);line-height:1}
.service p{position:absolute;width:404px;font-size:18px;line-height:24px;text-align:justify;color:var(--text)}
.btn-estimate{position:absolute;width:235px;height:54px;background:var(--green);color:var(--white);font-size:18px;font-weight:500;display:flex;align-items:center;justify-content:center;border-radius:2px}
.photo{position:absolute;border-radius:50%}
.deco{position:absolute}
.site-footer{position:absolute;left:0;top:2911px;width:1200px;height:510px;background:var(--navy)}
.site-footer h3{position:absolute;top:72px;font-family:"Oswald",sans-serif;font-weight:500;font-size:24px;color:var(--white)}
.site-footer ul{position:absolute;list-style:none}
.site-footer li{font-size:14.5px;color:var(--white);height:32px;line-height:20px;padding-left:14px;position:relative}
.site-footer li::before{content:"+";position:absolute;left:0;top:0;color:var(--green);font-size:13px}
.contact-item{position:absolute;left:904px;display:flex;gap:12px;font-size:14.5px;line-height:19px;color:var(--white)}
.contact-item svg{flex:none}
.copyright{position:absolute;left:0;top:3421px;width:1200px;height:47px;background:var(--green);color:var(--white);font-size:13.5px}
.copyright span{position:absolute;left:62px;top:15px}
.social{position:absolute;top:13px;width:20px;height:20px;border-radius:50%;border:2px solid var(--white)}
</style>
</head>
<body>
<svg width="0" height="0" style="position:absolute">
  <symbol id="sparkle" viewBox="0 0 20 20"><path d="M10 0 L11.6 8.4 L20 10 L11.6 11.6 L10 20 L8.4 11.6 L0 10 L8.4 8.4 Z" fill="#76bd43"/></symbol>
  <symbol id="ring" viewBox="0 0 20 20"><circle cx="10" cy="10" r="8" fill="none" stroke="#76bd43" stroke-width="2"/></symbol>
  <symbol id="ring-faint" viewBox="0 0 20 20"><circle cx="10" cy="10" r="8" fill="none" stroke="#3a5ea6" stroke-width="2"/></symbol>
</svg>

<header class="site-header">
  <div class="brand"><span class="brand-dot"></span>BrightNest</div>
  <span class="nav-mark">+</span>
  <nav class="main-nav">
    <a style="left:292px">Home</a>
    <a style="left:354px" class="active">Services</a>
    <a style="left:432px">What's Included</a>
    <a style="left:558px">For Realtors</a>
    <a style="left:657px">Blog</a>
  </nav>
  <div class="btn-phone">
    <svg width="16" height="16" viewBox="0 0 24 24" fill="none" stroke="#fff" stroke-width="2"><path d="M22 16.9v3a2 2 0 0 1-2.2 2 19.8 19.8 0 0 1-8.6-3.1 19.5 19.5 0 0 1-6-6A19.8 19.8 0 0 1 2.1 4.2 2 2 0 0 1 4.1 2h3a2 2 0 0 1 2 1.7c.1 1 .4 1.9.7 2.8a2 2 0 0 1-.5 2.1L8 9.9a16 16 0 0 0 6 6l1.3-1.3a2 2 0 0 1 2.1-.4c.9.3 1.8.6 2.8.7a2 2 0 0 1 1.7 2z"/></svg>
    +123 456 7890
  </div>
  <div class="btn-header">Get a Free Estimate</div>
</header>

<section class="hero" role="img" aria-label="Cleaner holding a mop and cleaning supplies in a living room, under a blue tint">
  <h1>Available Cleaning Services</h1>
</section>

<section class="service" style="top:466px;height:605px">
  <h2 style="left:125px;top:184px">Pre-Sale Cleaning</h2>
  <p style="left:125px;top:238px">Let us take the stress out of preparing your home for sale. First impressions matter; a clean and fresh home can make a huge difference.</p>
  <div class="btn-estimate" style="left:125px;top:346px">Get a Free Estimate</div>
  <div class="photo" role="img" aria-label="Smiling cleaner in an apron holding a vacuum hose" style="left:675px;top:103px;width:398px;height:398px;background:radial-gradient(circle at 45% 40%,#f2f2f2,#d9dbe0)"></div>
  <svg class="deco" style="left:647px;top:158px" width="16" height="16"><use href="#sparkle"/></svg>
  <svg class="deco" style="left:29px;top:290px" width="18" height="18"><use href="#ring"/></svg>
  <svg class="deco" style="left:1096px;top:348px" width="22" height="22"><use href="#ring"/></svg>
  <svg class="deco" style="left:350px;top:482px" width="16" height="16"><use href="#sparkle"/></svg>
</section>

<section class="service alt" style="top:1071px;height:605px">
  <div class="photo" role="img" aria-label="Cleaner crouching to sweep the floor with a brush and dustpan" style="left:134px;top:98px;width:398px;height:398px;background:radial-gradient(circle at 50% 45%,#f0f0f0,#cfd3da)"></div>
  <h2 style="left:669px;top:172px">Move-In Cleaning</h2>
  <p style="left:669px;top:227px">Moving doesn't have to be a stressful experience. Let us take the hassle out of your move and ensure your new Barrie home is clean, fresh, and ready for you to settle in.</p>
  <div class="btn-estimate" style="left:669px;top:361px">Get a Free Estimate</div>
  <svg class="deco" style="left:514px;top:112px" width="22" height="22"><use href="#ring"/></svg>
  <svg class="deco" style="left:1100px;top:101px" width="16" height="16"><use href="#sparkle"/></svg>
  <svg class="deco" style="left:70px;top:373px" width="16" height="16"><use href="#sparkle"/></svg>
  <svg class="deco" style="left:976px;top:509px" width="18" height="18"><use href="#ring"/></svg>
</section>

<section class="service" style="top:1676px;height:629px">
  <h2 style="left:125px;top:168px">Move-Out Cleaning</h2>
  <p style="left:125px;top:222px">Looking for a professional move-out cleaning service to ensure that your property is left sparkling clean and ready for the next occupants? Look no further than our expert team of cleaning professionals!</p>
  <div class="btn-estimate" style="left:125px;top:386px">Get a Free Estimate</div>
  <div class="photo" role="img" aria-label="Person mopping a wooden floor in a bright kitchen" style="left:649px;top:94px;width:426px;height:426px;background:radial-gradient(circle at 50% 40%,#efe9e3,#b9aa9b)"></div>
  <svg class="deco" style="left:649px;top:132px" width="22" height="22"><use href="#ring"/></svg>
  <svg class="deco" style="left:46px;top:236px" width="16" height="16"><use href="#sparkle"/></svg>
  <svg class="deco" style="left:1140px;top:321px" width="16" height="16"><use href="#sparkle"/></svg>
  <svg class="deco" style="left:503px;top:485px" width="18" height="18"><use href="#ring"/></svg>
</section>

<section class="service alt" style="top:2305px;height:606px">
  <div class="photo" role="img" aria-label="Cardboard boxes and a box of cleaning supplies" style="left:126px;top:105px;width:398px;height:398px;background:radial-gradient(circle at 50% 45%,#c9a57c,#9a7651)"></div>
  <h2 style="left:671px;top:154px">Junk &amp; Clutter Removal</h2>
  <p style="left:671px;top:208px">Over time, every household will accumulate several unwanted items that collect dust and take up space. Take advantage of our professional junk removal service to clean out your Barrie home, basement, garage, or any other storage area of unwanted items.</p>
  <div class="btn-estimate" style="left:671px;top:395px">Get a Free Estimate</div>
  <svg class="deco" style="left:931px;top:82px" width="16" height="16"><use href="#sparkle"/></svg>
  <svg class="deco" style="left:74px;top:174px" width="22" height="22"><use href="#ring"/></svg>
  <svg class="deco" style="left:1127px;top:456px" width="18" height="18"><use href="#ring"/></svg>
  <svg class="deco" style="left:501px;top:501px" width="16" height="16"><use href="#sparkle"/></svg>
</section>

<footer class="site-footer">
  <svg class="deco" style="left:591px;top:248px" width="32" height="32"><use href="#ring-faint"/></svg>
  <svg class="deco" style="left:1139px;top:282px" width="26" height="26"><use href="#ring-faint"/></svg>
  <svg class="deco" style="left:732px;top:373px" width="26" height="26"><use href="#ring-faint"/></svg>
  <svg class="deco" style="left:32px;top:433px" width="20" height="20"><use href="#ring-faint"/></svg>

  <h3 style="left:63px">Areas We Serve</h3>
  <ul style="left:63px;top:126px">
    <li>Alliston</li><li>Angus</li><li>Barrie</li><li>Coldwater</li><li>Collingwood</li><li>Creemore</li><li>Horseshoe Valley</li><li>Innisfil</li><li>Midland</li>
  </ul>
  <ul style="left:214px;top:126px">
    <li>Minesing</li><li>New Lowell</li><li>Orillia</li><li>Oro-Medonte</li><li>Shanty Bay</li><li>Springwater</li><li>Stayner</li><li>Wasaga</li><li>And everywhere<br>in between</li>
  </ul>

  <h3 style="left:481px">Availability</h3>
  <ul style="left:481px;top:126px">
    <li>Open 7 Days a Week (Monday-Sunday)</li>
    <li>Hours 8:00 am - 9:00 pm</li>
    <li>Evenings &amp; Weekends (Yes)</li>
  </ul>

  <h3 style="left:904px">Contact Us</h3>
  <div class="contact-item" style="top:126px">
    <svg width="22" height="24" viewBox="0 0 24 24" fill="none" stroke="#76bd43" stroke-width="1.6"><path d="M12 22s7-6.5 7-12a7 7 0 0 0-14 0c0 5.5 7 12 7 12z"/><circle cx="12" cy="10" r="2.6"/></svg>
    <span>123 Your Address Goes Here,<br>Barrie, Canada</span>
  </div>
  <div class="contact-item" style="top:186px">
    <svg width="22" height="22" viewBox="0 0 24 24" fill="none" stroke="#76bd43" stroke-width="1.6"><path d="M22 16.9v3a2 2 0 0 1-2.2 2 19.8 19.8 0 0 1-8.6-3.1 19.5 19.5 0 0 1-6-6A19.8 19.8 0 0 1 2.1 4.2 2 2 0 0 1 4.1 2h3a2 2 0 0 1 2 1.7c.1 1 .4 1.9.7 2.8a2 2 0 0 1-.5 2.1L8 9.9a16 16 0 0 0 6 6l1.3-1.3a2 2 0 0 1 2.1-.4c.9.3 1.8.6 2.8.7a2 2 0 0 1 1.7 2z"/></svg>
    <span>+123 456 7890</span>
  </div>
  <div class="contact-item" style="top:232px">
    <svg width="26" height="20" viewBox="0 0 26 20" fill="none" stroke="#76bd43" stroke-width="1.6"><rect x="1" y="1" width="24" height="18" rx="1"/><path d="M1 2l12 9 12-9"/></svg>
    <span>hello@brightnest.ca</span>
  </div>
</footer>

<div class="copyright">
  <span>Copyright© 2023 BrightNest. All rights reserved.</span>
  <div class="social" style="left:1088px"></div>
  <div class="social" style="left:1118px"></div>
</div>
</body>
</html>
```